Web Design Project

Hi everyone

Thanks for taking the time to read about this project.

Website needed for Corvel, female singer/songwriter and performer who is launching her debut album this year. She writes and performs folk/pop/soft rock music and plays guitar and piano.

see vidrelay links for examples of Corvel's style:
http://www.vidrelay.example/watch?v=Qp3TzL8wRn2
http://www.vidrelay.example/watch?v=Hk7DbVu4sYe

Looking for a classy, modern feel to the website. Cool colours are preferred but open to ideas. It needs it to have CoinTrove set up so items can be purchased from the site. The theme will be continued to Friendspace and business cards.

Examples include:

http://www.belindacrosshaw.example/

http://tessavorlund.example/

http://www.juneqtunes.example/home

Pages and content to be included:

HOME - main picture and general content

BIO - written content about Corvel

NEWS - this will be regularly updated, blog style

GIGS - this will be regularly updated

GALLERY - content will be photos only

SEE AND HEAR - content will be Videos and audios

STORE - this will have a cointrove function for purchase of CD and merchandise

GENEROSITY - this page will be devoted to charity work and updated regularly

CONTACT - information on how to contact Corvel's management

Buttons will need to provide links to VidRelay, Chirpline, Friendspace, Snapwell

I will work closely with the designers in giving feedback as ideas are generated and then provide further content such as photos and videos.

Thanks for considering this project!
Updates

HI everyone thanks for all your submissions so far. Please note the following:

- photos have been uploaded to assist with themes

- background could be a solid colour or texture (e.g. tree trunk texture)

- please use a hand writing font similar to Fontaro font "Lift Our Voice" - doesn't have to be exactly this but similar

Thank you,

Corvel

Hi again everyone

I apologise but the pixel bazaar website won't allow me to upload files. I will attempt to correct this as soon as possible. Thanks                                   

Target Market(s)

18-55 year olds who appreciate this genre of music; gay and lesbian community

Industry/Entity Type

Charity

Requirements
Should not have
• No flowers or flowery themes

```html
<!DOCTYPE html>
<html lang="en">
<head>
<meta charset="utf-8">
<title>Corvel — Singer / Songwriter</title>
<link href="https://fonts.googleapis.com/css2?family=Raleway:wght@300;400;600;700&family=Josefin+Slab:wght@400;600&display=swap" rel="stylesheet">
<style>
:root{
  --red:#d2412e;
  --cream:#f1ece2;
  --cream-dark:#e6dfd1;
  --teal:#86abad;
  --teal-dark:#5f8789;
  --purple:#b79ac3;
  --green:#8ba87c;
  --green-dark:#6f8f60;
  --green-btn:#a9c48e;
  --taupe:#a7a08c;
  --ink:#4a4640;
  --muted:#8d877c;
  --white:#ffffff;
}
*{margin:0;padding:0;box-sizing:border-box}
html,body{width:1200px;height:2264px;overflow:hidden}
body{background:var(--cream);font-family:'Raleway',sans-serif;color:var(--ink);position:relative}
.abs{position:absolute}

/* hero */
.hero{left:0;top:0;width:1200px;height:640px;
  background:radial-gradient(ellipse at 30% 45%,#6b4a33 0%,#2e211a 40%,#120c09 100%)}
.hero-stripe{left:0;top:0;width:1200px;height:8px;background:var(--red)}
.hero-photo-left{left:150px;top:40px;width:330px;height:600px;border-radius:40px 40px 0 0;
  background:linear-gradient(180deg,#3a2a20 0%,#5b4030 55%,#7a5a3e 100%);opacity:.85}
.hero-photo-right{left:560px;top:170px;width:560px;height:470px;border-radius:60px 60px 0 0;
  background:radial-gradient(ellipse at 50% 40%,#9a6d4a 0%,#4a3122 60%,#1c130e 100%);opacity:.9}
.logo{right:42px;top:34px;font-family:'Raleway',sans-serif;font-weight:600;font-size:64px;color:#e8c48e;letter-spacing:1px}
.nav{left:338px;top:108px;display:flex;gap:0;font-size:15px;font-weight:700;color:var(--white);letter-spacing:.5px}
.nav a{color:inherit;text-decoration:none;padding:8px 12px}
.nav a.active{background:var(--red)}
.social-rail{left:1152px;top:196px;display:flex;flex-direction:column;gap:14px}
.social-rail span{display:block;width:36px;height:36px;border-radius:50%;background:#b6453a}
.slider-dots{left:1124px;top:614px;display:flex;gap:6px}
.slider-dots span{width:12px;height:12px;border-radius:50%;background:#8f857a}
.slider-dots span.on{background:var(--red)}

/* welcome */
.welcome{left:0;top:640px;width:1200px;height:300px;background:var(--cream)}
.portrait-main{left:148px;top:30px;width:184px;height:184px;border-radius:50%;border:8px solid var(--white);
  background:radial-gradient(circle at 45% 40%,#c59b76,#6b4b36);box-shadow:0 2px 6px rgba(0,0,0,.15)}
.portrait-small{left:240px;top:180px;width:96px;height:96px;border-radius:50%;border:6px solid var(--white);
  background:radial-gradient(circle at 50% 40%,#a98466,#4d3628)}
.welcome h1{left:420px;top:32px;font-family:'Josefin Slab',serif;font-weight:600;font-size:58px;color:var(--teal)}
.welcome p{left:420px;top:104px;width:740px;font-size:13.5px;line-height:20px;color:var(--muted)}

/* media */
.section-head{font-family:'Raleway',sans-serif;font-weight:300;font-size:44px;color:var(--teal);display:flex;align-items:center;gap:14px}
.section-head .rule{flex:1;height:3px;background:var(--teal)}
.videos-head{left:140px;top:958px;width:440px}
.photos-head{left:620px;top:958px;width:440px}
.video-player{left:140px;top:1020px;width:440px;height:312px;background:#1a1714}
.video-frame{left:0;top:0;width:440px;height:282px;background:radial-gradient(ellipse at 55% 45%,#8a7560,#3a2d24 70%)}
.video-bar{left:0;top:282px;width:440px;height:30px;background:#24211e}
.photo-grid{left:620px;top:1020px;width:440px;display:grid;grid-template-columns:repeat(4,1fr);gap:12px}
.photo-grid span{height:100px;border:3px solid var(--white);background:linear-gradient(160deg,#8c6a4e,#3b2b21)}
.photo-grid span:nth-child(2n){background:linear-gradient(160deg,#a88766,#4b3829)}
.gallery-btn{left:620px;top:1256px;width:440px;height:40px;background:var(--purple);color:var(--white);
  font-size:16px;font-weight:600;display:flex;align-items:center;justify-content:center}

/* shop */
.shop{left:0;top:1370px;width:1200px;height:330px;background:var(--green)}
.shop-head{left:140px;top:34px;width:920px;color:var(--white)}
.shop-head .rule{background:var(--white)}
.products{left:140px;top:104px;display:flex;gap:22px}
.product{width:166px}
.product-img{width:166px;height:130px;border:4px solid var(--white);background:linear-gradient(160deg,#8f6e52,#3e2e23)}
.product-name{margin-top:8px;font-size:14px;color:var(--white);font-weight:600}
.product-btn{margin-top:6px;width:70px;height:22px;background:var(--green-btn);color:var(--white);font-size:11px;font-weight:700;display:flex;align-items:center;justify-content:center}

/* social + testimonial */
.chirp-head{left:140px;top:1722px;width:440px}
.chirp-head .handle{font-size:16px;color:var(--muted);font-weight:400}
.chirp-dot{width:36px;height:36px;border-radius:50%;background:var(--teal)}
.tweets{left:140px;top:1800px;width:440px}
.tweet{font-size:13px;line-height:19px;color:var(--ink);margin-bottom:22px}
.tweet-meta{display:flex;justify-content:space-between;font-size:11px;color:var(--muted);margin-top:4px}
.tweet-meta .actions{display:flex;gap:14px}
.testi-head{left:620px;top:1722px;width:440px}
.testi-quote{font-family:'Josefin Slab',serif;font-size:90px;line-height:60px;color:#c99a4e;height:44px}
.testimonial{left:620px;top:1800px;width:440px;font-size:13px;line-height:19px;color:var(--ink)}
.testimonial .credit{margin-top:14px;text-align:right;padding-right:80px;color:var(--muted)}

/* footer */
.footer{left:0;top:2110px;width:1200px;height:154px;background:var(--taupe);color:var(--white)}
.footer-nav{left:0;top:26px;width:1200px;display:flex;justify-content:center;gap:30px;font-size:13px;font-weight:700}
.footer-social{left:0;top:66px;width:1200px;display:flex;justify-content:center;gap:14px}
.footer-social span{width:38px;height:38px;border-radius:50%;border:2px solid var(--white)}
.copyright{left:0;top:124px;width:1200px;text-align:center;font-size:11px;letter-spacing:.5px}
</style>
</head>
<body>

<header class="abs hero">
  <div class="abs hero-photo-left" role="img" aria-label="Photo of the singer seated with a hand drum"></div>
  <div class="abs hero-photo-right" role="img" aria-label="Photo of the singer performing at a microphone"></div>
  <div class="abs hero-stripe"></div>
  <div class="abs logo">Corvel</div>
  <nav class="abs nav">
    <a class="active" href="#">HOME</a><a href="#">BIO</a><a href="#">NEWS</a><a href="#">GIGS</a><a href="#">GALLERY</a><a href="#">SEE AND HEAR</a><a href="#">STORE</a><a href="#">GENEROSITY</a><a href="#">CONTACT</a>
  </nav>
  <div class="abs social-rail" aria-label="Social links"><span></span><span></span><span></span><span></span><span></span></div>
  <div class="abs slider-dots"><span class="on"></span><span></span><span></span></div>
</header>

<section class="abs welcome">
  <div class="abs portrait-main" role="img" aria-label="Portrait of the singer with a guitar"></div>
  <div class="abs portrait-small" role="img" aria-label="Smaller portrait of the singer"></div>
  <h1 class="abs">Welcome to Corvel</h1>
  <p class="abs">Corvel writes songs about open roads, small towns and the people who carry us through long winters. Raised between a piano bench and a borrowed guitar, she began playing coffee houses at sixteen and never stopped. Her sound blends folk storytelling with warm pop melodies and the quiet edge of soft rock. This year she releases her debut album, recorded live with friends over three cold weeks in a converted barn. Every track was captured in a handful of takes so the room, the breath and the mistakes all stay in. When she is not on stage, Corvel gives her time to local shelters and music programs for young people who need a place to be heard. Thank you for stopping by, and welcome to the music.</p>
</section>

<h2 class="abs section-head videos-head">Recent Videos <span class="rule"></span>
  <svg width="34" height="30" viewBox="0 0 34 30"><rect x="1" y="6" width="32" height="22" fill="none" stroke="#86abad" stroke-width="3"/><path d="M10 1l7 5 7-5" fill="none" stroke="#86abad" stroke-width="3"/></svg>
</h2>
<div class="abs video-player">
  <div class="abs video-frame" role="img" aria-label="Video still of the singer playing guitar"></div>
  <div class="abs video-bar">
    <svg width="440" height="30" viewBox="0 0 440 30"><path d="M12 9l10 6-10 6z" fill="#fff"/><rect x="34" y="13" width="330" height="4" fill="#555"/><rect x="34" y="13" width="90" height="4" fill="#d2412e"/><rect x="380" y="10" width="18" height="10" fill="none" stroke="#fff" stroke-width="2"/><rect x="408" y="10" width="20" height="10" fill="#fff"/></svg>
  </div>
</div>

<h2 class="abs section-head photos-head">Photos <span class="rule"></span>
  <svg width="32" height="30" viewBox="0 0 32 30"><rect x="1" y="1" width="30" height="28" fill="none" stroke="#b79ac3" stroke-width="3"/><path d="M4 26l9-11 6 7 4-4 6 8z" fill="#b79ac3"/></svg>
</h2>
<div class="abs photo-grid" role="img" aria-label="Gallery of eight photos of the singer">
  <span></span><span></span><span></span><span></span><span></span><span></span><span></span><span></span>
</div>
<div class="abs gallery-btn">View Gallery</div>

<section class="abs shop">
  <h2 class="abs section-head shop-head">Shop <span class="rule"></span></h2>
  <div class="abs products">
    <div class="product"><div class="product-img" role="img" aria-label="Album cover"></div><div class="product-name">Album Name</div><div class="product-btn">BUY NOW</div></div>
    <div class="product"><div class="product-img" role="img" aria-label="Album cover"></div><div class="product-name">Album Name</div><div class="product-btn">BUY NOW</div></div>
    <div class="product"><div class="product-img" role="img" aria-label="Album cover"></div><div class="product-name">Album Name</div><div class="product-btn">BUY NOW</div></div>
    <div class="product"><div class="product-img" role="img" aria-label="Album cover"></div><div class="product-name">Album Name</div><div class="product-btn">BUY NOW</div></div>
    <div class="product"><div class="product-img" role="img" aria-label="Album cover"></div><div class="product-name">Album Name</div><div class="product-btn">BUY NOW</div></div>
  </div>
</section>

<h2 class="abs section-head chirp-head">Chirpline <span class="handle">@corvel</span><span class="rule"></span><span class="chirp-dot"></span></h2>
<div class="abs tweets">
  <div class="tweet">New single rehearsals start tonight, thank you for all the kind messages this week http://shortlnk.example/4xR2
    <div class="tweet-meta"><span>7 hours ago</span><span class="actions"><span>Reply</span><span>Retweet</span><span>Favorite</span></span></div></div>
  <div class="tweet">Tickets for the spring album launch show are now on sale, see you there friends http://shortlnk.example/8mQ1
    <div class="tweet-meta"><span>7 hours ago</span><span class="actions"><span>Reply</span><span>Retweet</span><span>Favorite</span></span></div></div>
  <div class="tweet">A big thank you to everyone who came to the shelter benefit night, we raised so much http://shortlnk.example/3kT7
    <div class="tweet-meta"><span>7 hours ago</span><span class="actions"><span>Reply</span><span>Retweet</span><span>Favorite</span></span></div></div>
</div>

<h2 class="abs section-head testi-head">Testimonial <span class="rule"></span><span class="testi-quote">&ldquo;</span></h2>
<div class="abs testimonial">
  <p>“I first heard Corvel in a tiny bar on a rainy Tuesday and left with a song stuck in my head for a week. Her voice is honest and warm, and her lyrics feel like letters from an old friend. Seeing her live is something special; the whole room goes quiet when she starts to play. I cannot wait to hear the new album and to follow wherever the music takes her next.”</p>
  <p class="credit">- Mara Ellis</p>
</div>

<footer class="abs footer">
  <nav class="abs footer-nav"><span>HOME</span><span>BIO</span><span>NEWS</span><span>GIGS</span><span>GALLERY</span><span>SEE AND HEAR</span><span>STORE</span><span>GENEROSITY</span><span>CONTACT</span></nav>
  <div class="abs footer-social" aria-label="Social links"><span></span><span></span><span></span><span></span><span></span></div>
  <div class="abs copyright">COPYRIGHT © 2014 CORVEL. ALL RIGHTS RESERVED.</div>
</footer>

</body>
</html>
```